Creative Brief
Marketing Collateral for Real Estate Business
Create matching postcards and Business Card.
MARKETING COLLATERAL FOR REAL ESTATE COMPANY
Create matching postcards, HTML email template and Business Card.
Postcard (5.5” x 8.5”) template
Email HTML template
Business Card
DESCRIPTION
Our office needs 2-3 “Just Listed” postcard templates for REAL ESTATE FORECLOSURE LISITNGS. The templates must display two logos which are provided (FindMarlowHomesteads.example to be large in size). We need the ability to insert pictures of each new listing inside within the template. The design must be colorful (earth tone colors), professional, simple and eye catching. Postcard: We also want 1-2 generic postcard templates where a standard/general real estate picture is already inserted which can be used for multiple/different properties.
Postcard templates must meet the printing specifications for PressNook.example. The templates must be provided in digital formats that are editable by the project holder. They must also be provided in print ready formats. Our company is based in Marlow, SC, USA. Please view images of Marlow, SC, USA via google if necessary for the postcard template.
The HTML Email Template(s) will be used to mass email our database with new listings.
Real Estate
Buyers of Real Estate Foreclosed Properties; Real Estate Investors.
DESIGN
POSTCARD COMMENTS / STATEMENTS TO BE INCLUDED WITHIN THE POSTCARD / EMAIL HTML
-PRE-LISTING(1-2 Templates)
-JUST LISTED (1-2 Templates)
-SEARCH HUNDREDS OF BANK OWNED FORECLOSURES – SIGN UP FREE! FINDMARLOWHOMESTEADS.EXAMPLE
-Join FindMarlowHomesteads.example and be the first to know about newly listed Marlow Foreclosures.
-Don’t miss this opportunity to buy a bank owned foreclosure.
-We are your Marlow Foreclosure Specialist!
-NEW LISTING ALERT – Sign up and receive listings meeting your criteria today! (in a highlighted icon or box or similar)
-This property is NOT listed in MLS yet. Please contact me if you are interested in purchasing this property. (disclaimer/small font))
POSTCARD SIZE
Postcard 5.5” x 8.5”
COLORS
Blue / Green / Tan (Earth tone colors) / To match FindMarlowHomesteads.example logo
Color (front and back)
Images and Date to be used

```html
<!DOCTYPE html>
<html lang="en">
<head>
<meta charset="utf-8">
<title>BrightHarbor – Postcard, Business Card and Email Signature Set</title>
<link rel="stylesheet" href="https://fonts.googleapis.com/css2?family=Montserrat:wght@400;600;700;800;900&family=Open+Sans:wght@400;600;700&display=swap">
<style>
:root{
  --stage:#3a3a3a;
  --stage-dark:#262626;
  --white:#ffffff;
  --paper:#fbfbf8;
  --navy:#173f7a;
  --blue:#1f6fb5;
  --sky:#5aa6de;
  --green:#6db33f;
  --lime:#9bcf4a;
  --orange:#f39a1e;
  --ink:#2b2b2b;
  --grey:#8a8f96;
}
*{box-sizing:border-box;margin:0;padding:0}
html,body{width:1200px;height:526px;overflow:hidden}
body{
  background:radial-gradient(ellipse at 50% 40%,var(--stage) 0%,var(--stage-dark) 100%);
  font-family:"Open Sans",Arial,sans-serif;color:var(--ink);position:relative;
}
.sheet-title{position:absolute;top:24px;left:0;width:100%;text-align:center;
  font:800 30px/1 "Montserrat",Arial,sans-serif;color:var(--white)}
.label{position:absolute;font:700 11px/1 "Montserrat",Arial,sans-serif;color:var(--white);white-space:nowrap}

.brand{position:absolute;display:flex;align-items:center;gap:4px;white-space:nowrap;
  font:700 11px/1 "Montserrat",Arial,sans-serif;color:var(--navy)}
.brand .dot{width:13px;height:13px;border-radius:50%;background:var(--green);flex:none}
.photo{position:absolute}
.house-photo{background:linear-gradient(180deg,#a9cbe8 0%,#dfe8ee 38%,#e9e2d2 55%,#b9a37e 72%,#6f8f4a 100%)}
.agent-photo{background:linear-gradient(180deg,#d9d4cc 0%,#9c8f80 35%,#4a4f58 70%,#2d3138 100%)}
.thumb-photo{background:linear-gradient(180deg,#b9d3e6,#d2c4a2 60%,#7e9c58);border:1px solid var(--white)}

/* ---------- postcards ---------- */
.postcard{position:absolute;height:192px;background:var(--paper);overflow:hidden;box-shadow:0 2px 6px rgba(0,0,0,.5)}
.postcard.front{width:324px}
.postcard.back{width:329px}
.postcard svg.wave{position:absolute;left:0;width:100%}

.front .brand{left:9px;top:10px}
.front .search-kicker{position:absolute;left:9px;top:56px;font:800 10px/1 "Montserrat",Arial,sans-serif;color:var(--navy)}
.front .search-headline{position:absolute;left:9px;top:67px;font:900 24px/1 "Montserrat",Arial,sans-serif;color:var(--blue)}
.front .search-sub{position:absolute;left:9px;top:93px;font:700 5.5px/1 "Montserrat",Arial,sans-serif;color:var(--green)}
.front .thumbs{position:absolute;left:9px;top:104px;display:flex;gap:4px}
.front .thumbs .thumb-photo{width:30px;height:20px}
.front svg.wave{bottom:0;height:80px}
.front .join{position:absolute;left:9px;bottom:12px;font:800 17px/1 "Montserrat",Arial,sans-serif;color:var(--white)}
.front .join-line{position:absolute;left:52px;bottom:13px;width:180px;font:600 5.5px/1.3 "Open Sans",Arial,sans-serif;color:var(--white)}

.back .stamp{position:absolute;right:9px;top:9px;width:28px;height:32px;border:1px dashed var(--grey)}
.back .disclaimer{position:absolute;left:160px;top:48px;width:140px;font:400 4.5px/1.3 "Open Sans",Arial,sans-serif;color:var(--grey)}
.back svg.wave{top:62px;height:44px}
.back .new-badge{position:absolute;left:5px;top:70px;width:28px;height:28px;border-radius:50%;
  background:var(--orange);color:var(--white);font:800 8px/28px "Montserrat",Arial,sans-serif;text-align:center}
.back .signup{position:absolute;left:9px;top:110px;font:800 11px/1 "Montserrat",Arial,sans-serif;color:var(--green)}
.back .signup-copy{position:absolute;left:9px;top:125px;width:92px;font:600 5.5px/1.35 "Open Sans",Arial,sans-serif;color:var(--navy)}
.back .address{position:absolute;left:190px;top:112px;width:120px}
.back .address span{display:block;height:1px;background:#cfd3d8;margin-bottom:11px}
.back .site{position:absolute;right:9px;bottom:26px;font:700 6px/1 "Montserrat",Arial,sans-serif;color:var(--navy)}
.back .specialist{position:absolute;left:0;bottom:0;width:100%;height:16px;background:var(--navy);
  color:var(--white);font:600 6.5px/16px "Open Sans",Arial,sans-serif;padding-left:36px}

/* ---------- business cards ---------- */
.bizcard{position:absolute;width:138px;height:77px;overflow:hidden;box-shadow:0 2px 5px rgba(0,0,0,.5)}
.bizcard svg{position:absolute;left:0;bottom:0;width:100%;height:30px}
.bizcard.face{background:var(--paper)}
.bizcard.face .brand{left:7px;top:9px;font-size:9px}
.bizcard.face .brand .dot{width:10px;height:10px}
.bizcard.face .contact{position:absolute;right:7px;top:24px;text-align:right;font:600 4.5px/1.45 "Open Sans",Arial,sans-serif;color:var(--navy)}
.bizcard.face .contact b{display:block;font:700 6px/1.3 "Montserrat",Arial,sans-serif}
.bizcard.reverse{display:flex;align-items:center;justify-content:center}
.bizcard.reverse.blue{background:linear-gradient(160deg,var(--sky),var(--blue) 55%,var(--navy))}
.bizcard.reverse.green{background:linear-gradient(160deg,var(--lime),var(--green) 60%,#4b8a2a)}
.bizcard.reverse .brand{position:relative;top:-6px;color:var(--white);font-size:10px}
.bizcard.reverse .brand .dot{background:var(--white)}

/* ---------- email signature ---------- */
.signature{position:absolute;width:159px;height:64px;background:var(--white);box-shadow:0 2px 5px rgba(0,0,0,.5);overflow:hidden}
.signature .brand{left:7px;top:9px;font-size:8px}
.signature .brand .dot{width:9px;height:9px}
.signature .sig-text{position:absolute;left:7px;top:26px;font:600 4.5px/1.4 "Open Sans",Arial,sans-serif;color:var(--navy)}
.signature .sig-agent{position:absolute;left:82px;top:8px;width:16px;height:40px}
.signature .sig-head{position:absolute;right:7px;top:14px;text-align:right;font:700 5px/1.3 "Montserrat",Arial,sans-serif;color:var(--navy)}
.signature .sig-head b{display:block;font:900 10px/1 "Montserrat",Arial,sans-serif;color:var(--blue)}
.signature svg{position:absolute;left:0;bottom:0;width:100%;height:12px}
</style>
</head>
<body>

<h1 class="sheet-title">Post Card</h1>

<span class="label" style="left:36px;top:68px">Front</span>
<span class="label" style="left:391px;top:68px">Back</span>
<span class="label" style="left:36px;top:286px">Front</span>
<span class="label" style="left:391px;top:286px">Back</span>
<span class="label" style="left:751px;top:76px">Business Card Front</span>
<span class="label" style="left:842px;top:178px">Business Card Back</span>
<span class="label" style="left:1003px;top:135px">Email Signature</span>
<span class="label" style="left:751px;top:291px">Business Card Front</span>
<span class="label" style="left:842px;top:394px">Business Card Back</span>
<span class="label" style="left:1003px;top:351px">Email Signature</span>

<!-- Row 1 postcard front -->
<section class="postcard front" style="left:36px;top:84px">
  <div class="photo house-photo" role="img" aria-label="Two-storey house with lawn" style="left:72px;top:0;width:185px;height:140px"></div>
  <div class="photo agent-photo" role="img" aria-label="Real estate agent in a suit giving a thumbs up" style="left:256px;top:0;width:68px;height:192px"></div>
  <div class="brand"><span class="dot"></span>BrightHarbor</div>
  <div class="search-kicker">SEARCH</div>
  <div class="search-headline">HUNDREDS</div>
  <div class="search-sub">OF BANK OWNED FORECLOSURES</div>
  <div class="thumbs">
    <div class="thumb-photo" role="img" aria-label="Listing photo"></div>
    <div class="thumb-photo" role="img" aria-label="Listing photo"></div>
  </div>
  <svg class="wave" viewBox="0 0 324 80" preserveAspectRatio="none">
    <path d="M0 28 C90 8 170 38 256 18 L256 80 L0 80Z" fill="var(--green)"/>
    <path d="M0 40 C90 20 170 50 256 30 L256 80 L0 80Z" fill="var(--blue)"/>
  </svg>
  <div class="join">Join</div>
  <div class="join-line">FindMarlowHomesteads.example and be the first to know about new Marlow foreclosures.</div>
</section>

<!-- Row 1 postcard back -->
<section class="postcard back" style="left:391px;top:84px">
  <div class="photo house-photo" role="img" aria-label="Faded house photo" style="left:0;top:0;width:150px;height:80px;opacity:.55"></div>
  <div class="stamp"></div>
  <div class="disclaimer">This property is NOT listed in MLS yet. Please contact me if interested.</div>
  <svg class="wave" viewBox="0 0 329 44" preserveAspectRatio="none">
    <path d="M0 10 C110 34 220 0 329 16 L329 24 C220 8 110 42 0 20Z" fill="var(--green)"/>
    <path d="M0 22 C110 44 220 12 329 26 L329 34 C220 22 110 54 0 32Z" fill="var(--blue)"/>
  </svg>
  <div class="new-badge">NEW</div>
  <div class="photo agent-photo" role="img" aria-label="Agent standing full length" style="left:110px;top:68px;width:28px;height:104px"></div>
  <div class="signup">SIGN UP</div>
  <div class="signup-copy">New listing alert – receive listings meeting your criteria today!</div>
  <div class="address"><span></span><span></span><span></span></div>
  <div class="site">www.findmarlowhomesteads.example</div>
  <div class="specialist">We are your Marlow Foreclosure Specialist!</div>
</section>

<!-- Row 2 postcard front -->
<section class="postcard front" style="left:36px;top:302px">
  <div class="photo house-photo" role="img" aria-label="Two-storey house with lawn" style="left:72px;top:0;width:185px;height:140px"></div>
  <div class="photo agent-photo" role="img" aria-label="Real estate agent in a suit giving a thumbs up" style="left:256px;top:0;width:68px;height:192px"></div>
  <div class="brand"><span class="dot"></span>BrightHarbor</div>
  <div class="search-kicker">SEARCH</div>
  <div class="search-headline">HUNDREDS</div>
  <div class="search-sub">OF BANK OWNED FORECLOSURES</div>
  <div class="thumbs">
    <div class="thumb-photo" role="img" aria-label="Listing photo"></div>
    <div class="thumb-photo" role="img" aria-label="Listing photo"></div>
  </div>
  <svg class="wave" viewBox="0 0 324 80" preserveAspectRatio="none">
    <path d="M0 28 C90 8 170 38 256 18 L256 80 L0 80Z" fill="var(--blue)"/>
    <path d="M0 40 C90 20 170 50 256 30 L256 80 L0 80Z" fill="var(--green)"/>
  </svg>
  <div class="join">Join</div>
  <div class="join-line">FindMarlowHomesteads.example and be the first to know about new Marlow foreclosures.</div>
</section>

<!-- Row 2 postcard back -->
<section class="postcard back" style="left:391px;top:302px">
  <div class="photo house-photo" role="img" aria-label="Faded house photo" style="left:0;top:0;width:150px;height:80px;opacity:.55"></div>
  <div class="stamp"></div>
  <div class="disclaimer">This property is NOT listed in MLS yet. Please contact me if interested.</div>
  <svg class="wave" viewBox="0 0 329 44" preserveAspectRatio="none">
    <path d="M0 10 C110 34 220 0 329 16 L329 24 C220 8 110 42 0 20Z" fill="var(--blue)"/>
    <path d="M0 22 C110 44 220 12 329 26 L329 34 C220 22 110 54 0 32Z" fill="var(--green)"/>
  </svg>
  <div class="new-badge">NEW</div>
  <div class="photo agent-photo" role="img" aria-label="Agent standing full length" style="left:110px;top:68px;width:28px;height:104px"></div>
  <div class="signup">SIGN UP</div>
  <div class="signup-copy">New listing alert – receive listings meeting your criteria today!</div>
  <div class="address"><span></span><span></span><span></span></div>
  <div class="site">www.findmarlowhomesteads.example</div>
  <div class="specialist">We are your Marlow Foreclosure Specialist!</div>
</section>

<!-- Business cards row 1 -->
<section class="bizcard face" style="left:751px;top:91px">
  <div class="brand"><span class="dot"></span>BrightHarbor</div>
  <div class="contact"><b>Agent Name</b>Broker Associate<br>(555) 014-2270<br>agent@fmh.example</div>
  <svg viewBox="0 0 138 30" preserveAspectRatio="none">
    <path d="M0 14 C45 0 90 24 138 8 L138 30 L0 30Z" fill="var(--green)"/>
    <path d="M0 21 C45 7 90 30 138 16 L138 30 L0 30Z" fill="var(--blue)"/>
  </svg>
</section>
<section class="bizcard reverse blue" style="left:842px;top:193px">
  <div class="brand"><span class="dot"></span>BrightHarbor</div>
  <svg viewBox="0 0 138 30" preserveAspectRatio="none">
    <path d="M0 16 C45 2 90 26 138 10 L138 30 L0 30Z" fill="var(--green)"/>
  </svg>
</section>
<section class="signature" style="left:1003px;top:151px">
  <div class="brand"><span class="dot"></span>BrightHarbor</div>
  <div class="sig-text">Agent Name<br>(555) 014-2270</div>
  <div class="photo agent-photo sig-agent" role="img" aria-label="Agent portrait"></div>
  <div class="sig-head">SEARCH<b>HUNDREDS</b></div>
  <svg viewBox="0 0 159 12" preserveAspectRatio="none"><path d="M0 4 C50 0 110 8 159 2 L159 7 C110 12 50 4 0 9Z" fill="var(--green)"/><path d="M0 9 C50 4 110 12 159 7 L159 12 L0 12Z" fill="var(--blue)"/></svg>
</section>

<!-- Business cards row 2 -->
<section class="bizcard face" style="left:751px;top:306px">
  <div class="brand"><span class="dot"></span>BrightHarbor</div>
  <div class="contact"><b>Agent Name</b>Broker Associate<br>(555) 014-2270<br>agent@fmh.example</div>
  <svg viewBox="0 0 138 30" preserveAspectRatio="none">
    <path d="M0 14 C45 0 90 24 138 8 L138 30 L0 30Z" fill="var(--blue)"/>
    <path d="M0 21 C45 7 90 30 138 16 L138 30 L0 30Z" fill="var(--green)"/>
  </svg>
</section>
<section class="bizcard reverse green" style="left:842px;top:409px">
  <div class="brand"><span class="dot"></span>BrightHarbor</div>
  <svg viewBox="0 0 138 30" preserveAspectRatio="none">
    <path d="M0 16 C45 2 90 26 138 10 L138 30 L0 30Z" fill="var(--blue)"/>
  </svg>
</section>
<section class="signature" style="left:1003px;top:367px">
  <div class="brand"><span class="dot"></span>BrightHarbor</div>
  <div class="sig-text">Agent Name<br>(555) 014-2270</div>
  <div class="photo agent-photo sig-agent" role="img" aria-label="Agent portrait"></div>
  <div class="sig-head">SEARCH<b>HUNDREDS</b></div>
  <svg viewBox="0 0 159 12" preserveAspectRatio="none"><path d="M0 4 C50 0 110 8 159 2 L159 7 C110 12 50 4 0 9Z" fill="var(--blue)"/><path d="M0 9 C50 4 110 12 159 7 L159 12 L0 12Z" fill="var(--green)"/></svg>
</section>

</body>
</html>
```